Wine labels Velmora Wine Council - Nueva etiqueta El Consejo Regulador de vinos de Albarrán

Velmora Wines Council, based in southern Spain, are looking to create a new suite of wine labels which retain the elegance of the Sherry Wines industry while reinvigorating their image to the modern era and a new generation of Sherry Wine lovers. These labels will be used across the Velmora Wines Council's range of wines for the promotion of the Sherry Wines industry.

Your design must present at least two styles of Sherry Wines which demonstrate an elegant, modern interpretation and understanding of the unique mood and personality for these wines and the essence of southern Spain.

10 labels will be created based on the winning design, one for each of the unique varieties of Sherry Wines within the collection. This collection comprises of several different wine varieties including: Fino, Manzanilla, Amontillado, Oloroso, Palo Cortado, Medium, Cream, Pale Cream, Pedro Ximenez and Moscatel.

We recommend you visit our website www.velmora-vinos.example/wines as the source to understanding the origins and unique personality of these diverse wines.

El Consejo Regulador de los Vinos de Albarrán y Tordesal quiere renovar las etiquetas de los vinos utilizados para sus actividades de promoción genérica. Esta colección de vinos comprende las tipologías más importantes de la región que incluye: fino, manzanilla, amontillado, oloroso, palo cortado, pale cream, medium, cream, pedro ximénez y moscatel. Por lo tanto se precisan 10 etiquetas, una para cada uno de los vinos mencionados.
Updates

Project Deadline Extended
Reason: Due to some confusion with the deadline we wish to officially extend the deadline to allow designers one last week to submit their entries.

Target Market(s)

Industry, journalists, media, sommeliers, chefs, wine writers

Industry/Entity Type

Council

Requirements
Must have
• Front and Back label plus capsule:
• Front label can have either of the two official logos of the Velmora Wine council titled Vinos de Albarrán Digital or not, this is optional. Must include: Vino selecionado por el Consejo Regulador de la Denominacion de Origen, Name of the variety of wine eg FINO, percentage of alcohol eg 15% and quantity 75 cl.
• The back of the label must include the council logo titled Sellora and 4 additional logos positioned smaller. The Europa logo must appear larger than the 3 other logos. Space for descriptive text about the wine is also required.
• The dimensions of the bottle can be found at this link http://www.vidrialto.example/es/catalogo/vinos-y-espumosos/bordelesas/bd-orla
• Altura:305 mm
• Diámetro base:76,20 mm
• Diámetro hombro:82 mm
• Tipo boca:Cetie
• Peso:750 gr
• Capacidad:75 cl
• Etiqueta delantera y trasera y capsula
• La etiqueta delantera puede incluir el logo oficial del Consejo Regulador o el logo digital, o ninguno, esto es opcional. Debe incluir el siguiete texto: Vino selecionado por el Consejo Regulador de la Denominacion de Origen, el nombre de la variedad del vino, por ejemplo Fino, el porcentaje de alcohol, por ejemplo 15%, y la capacidad 75cl.
• La etiqueta trasera debe incluir el logo oficial Sellora del Consejo, y cuatro logos adicionales con una dimension menor. El Logo de ¨Europa invierte en las zonas rurales¨ debe ser de mayor tamaño que los otros. Se precisa espacio para el texto descriptivo de los vinos.
• Las dimensiones de la botella se puede encontrar en este enlace
• http://www.vidrialto.example/es/catalogo/vinos-y-espumosos/bordelesas/bd-orla
• Altura:305 mm
• Diámetro base:76,20 mm
• Diámetro hombro:82 mm
• Tipo boca:Cetie
• Peso:750 gr
• Capacidad:75 cl
Nice to have
• See our website velmora-vinos.example to understand the origin of the wines. Ver nuestra página web velmora-vinos.example para mejor entender los vinos.
Should not have
• Images of catavinos or stereotypical images from Spain such as flamenco dancers or guitars.

```html
<!DOCTYPE html>
<html lang="es">
<head>
<meta charset="utf-8">
<title>Diseño de Etiqueta – Consejo Regulador de Albarrán</title>
<link rel="stylesheet" href="https://fonts.googleapis.com/css2?family=Josefin+Slab:wght@400;600;700&family=Inter:wght@200;300;500;700&family=Gelasio:wght@400&display=swap">
<style>
  :root {
    --yellow: #FBD645;
    --amber: #E1A730;
    --maroon: #70181E;
    --sand: #E4D8C8;
    --cocoa: #2B1B0D;
    --ink: #111;
    --panel: #000;
    --paper: #fff;
    --rule: #cfcfcf;
  }
  * { margin: 0; padding: 0; box-sizing: border-box; }
  html, body { width: 1200px; height: 1000px; overflow: hidden; background: var(--paper); }
  .board { position: relative; width: 1200px; height: 1000px; font-family: "Josefin Slab", serif; color: var(--ink); }
  .abs { position: absolute; }

  /* Intro */
  .intro-title { left: 36px; top: 48px; font-size: 38px; font-weight: 700; }
  .intro-sub { left: 36px; top: 104px; font-size: 23px; }
  .intro-client { left: 36px; top: 142px; font-size: 31px; font-weight: 600; line-height: 46px; }
  .intro-wine-label { left: 36px; top: 284px; font-size: 24px; }
  .intro-wine { left: 36px; top: 320px; font-size: 36px; font-weight: 600; }

  /* Palette */
  .palette-title { left: 36px; top: 593px; font-size: 23px; font-weight: 600; text-decoration: underline; text-underline-offset: 3px; }
  .swatch-code { left: 45px; font-size: 24px; font-weight: 600; letter-spacing: .5px; }
  .swatch { left: 176px; width: 50px; height: 50px; }

  /* Typography list */
  .type-title { left: 773px; top: 36px; font-size: 24px; font-weight: 600; text-decoration: underline; text-underline-offset: 3px; }
  .type-sample { left: 780px; font-size: 24px; font-weight: 600; }

  /* Panels */
  .panel { background: var(--panel); }
  .dim-label { font-family: "Inter", sans-serif; font-size: 9px; font-weight: 300; color: #fff; background: var(--panel); padding: 0 2px; }

  /* Labels */
  .label { background: var(--paper); border-radius: 5px; overflow: hidden; }
  .sans { font-family: "Inter", sans-serif; }

  .front-bloom { left: 0; top: 12px; width: 170px; height: 170px; }
  .front-brand { left: 0; width: 170px; top: 108px; text-align: center; font-family: "Gelasio", serif; font-size: 12px; color: var(--maroon); letter-spacing: -.2px; }
  .variety-mark { background: var(--yellow); color: #fff; font-family: "Inter", sans-serif; font-weight: 200; display: flex; align-items: flex-end; }
  .variety-rest { font-family: "Inter", sans-serif; font-weight: 300; color: var(--ink); }
  .front-seal { left: 0; width: 170px; top: 292px; text-align: center; font-family: "Inter", sans-serif; font-weight: 300; line-height: 11px; }
  .front-seal .maroon { color: var(--maroon); font-size: 8px; }
  .front-seal .amber { color: var(--amber); font-size: 9.5px; }
  .front-spec { top: 344px; font-family: "Inter", sans-serif; font-weight: 700; font-size: 9px; }

  .back-copy { left: 11px; top: 48px; width: 148px; font-family: "Gelasio", serif; font-size: 7.1px; line-height: 8.6px; text-align: justify; hyphens: auto; color: var(--ink); }
  .back-copy p + p { margin-top: 8.6px; }
  .seal-name { font-family: "Gelasio", serif; font-size: 10px; letter-spacing: 1px; color: var(--cocoa); text-align: center; }
</style>
</head>
<body>
<main class="board">

  <!-- Intro -->
  <h1 class="abs intro-title">Diseño</h1>
  <p class="abs intro-sub">de Etiqueta para el</p>
  <p class="abs intro-client">Consejo Regulador<br>de Albarrán.</p>
  <p class="abs intro-wine-label">Vino elegido</p>
  <p class="abs intro-wine">Fino</p>

  <!-- Palette -->
  <h2 class="abs palette-title">Colores:</h2>
  <span class="abs swatch-code" style="top:658px;color:var(--yellow)">#FBD645</span>
  <div class="abs swatch" style="top:646px;background:var(--yellow)"></div>
  <span class="abs swatch-code" style="top:723px;color:var(--amber)">#E1A730</span>
  <div class="abs swatch" style="top:711px;background:var(--amber)"></div>
  <span class="abs swatch-code" style="top:788px;color:var(--maroon)">#70181E</span>
  <div class="abs swatch" style="top:776px;background:var(--maroon)"></div>
  <span class="abs swatch-code" style="top:853px;color:var(--sand)">#E4D8C8</span>
  <div class="abs swatch" style="top:841px;background:var(--sand)"></div>
  <span class="abs swatch-code" style="top:919px;color:var(--cocoa)">#2B1B0D</span>
  <div class="abs swatch" style="top:907px;background:var(--cocoa)"></div>

  <!-- Typography -->
  <h2 class="abs type-title">Tipografías de ejemplos:</h2>
  <p class="abs type-sample" style="top:91px">Halvora Neue 65 Medium</p>
  <p class="abs type-sample" style="top:136px">Halvora Neue 33 Thin Extended</p>
  <p class="abs type-sample" style="top:181px">Georgette Regular</p>

  <!-- Front label panel -->
  <section class="abs panel" style="left:340px;top:0;width:385px;height:706px;">
    <svg class="abs" style="left:0;top:0" width="385" height="706" aria-hidden="true">
      <g stroke="#fff" stroke-width=".7" fill="none">
        <line x1="108" y1="146" x2="276" y2="146"/>
        <polyline points="112,143 108,146 112,149"/>
        <polyline points="272,143 276,146 272,149"/>
        <line x1="80" y1="170" x2="80" y2="536"/>
        <polyline points="77,174 80,170 83,174"/>
        <polyline points="77,532 80,536 83,532"/>
      </g>
    </svg>
    <span class="abs dim-label" style="left:176px;top:131px">60 mm</span>
    <span class="abs dim-label" style="left:60px;top:345px">130 mm</span>

    <article class="abs label front-label" style="left:107px;top:170px;width:170px;height:366px;">
      <svg class="abs front-bloom" viewBox="0 0 170 170" role="img" aria-label="Mancha de acuarela amarilla">
        <defs>
          <radialGradient id="bloom" cx="50%" cy="50%" r="50%">
            <stop offset="0" stop-color="#FBD645" stop-opacity=".95"/>
            <stop offset=".7" stop-color="#FBD645" stop-opacity=".7"/>
            <stop offset="1" stop-color="#FBD645" stop-opacity=".15"/>
          </radialGradient>
        </defs>
        <circle cx="85" cy="88" r="82" fill="url(#bloom)"/>
      </svg>
      <p class="abs front-brand">VINOS DE ALBARRÁN</p>

      <div class="abs variety-mark" style="left:46px;top:209px;width:43px;height:67px;font-size:44px;padding:0 0 2px 6px;line-height:1;">F</div>
      <span class="abs variety-rest" style="left:91px;top:254px;font-size:17px;">ino</span>

      <p class="abs front-seal">
        <span class="maroon">VINOS SELECCIONADOS POR EL</span><br>
        <span class="amber">CONSEJO REGULADOR</span><br>
        <span class="maroon">DE LA DENOMINACIÓN DE ORIGEN</span>
      </p>
      <span class="abs front-spec" style="left:13px">75cl.</span>
      <span class="abs front-spec" style="right:13px">15%vol.</span>
    </article>
  </section>

  <!-- Capsule -->
  <svg class="abs capsule" style="left:440px;top:776px" width="290" height="146" aria-label="Cápsula" role="img">
    <polygon points="2,2 285,2 285,142 15,142" fill="var(--cocoa)"/>
    <rect x="15" y="134" width="270" height="8" fill="var(--yellow)"/>
    <line x1="29" y1="2" x2="29" y2="134" stroke="var(--sand)" stroke-width=".8"/>
  </svg>

  <!-- Back label panel -->
  <section class="abs panel" style="left:772px;top:293px;width:385px;height:707px;">
    <svg class="abs" style="left:0;top:0" width="385" height="707" aria-hidden="true">
      <g stroke="#fff" stroke-width=".7" fill="none">
        <line x1="108" y1="147" x2="277" y2="147"/>
        <polyline points="112,144 108,147 112,150"/>
        <polyline points="273,144 277,147 273,150"/>
        <line x1="81" y1="169" x2="81" y2="536"/>
        <polyline points="78,173 81,169 84,173"/>
        <polyline points="78,532 81,536 84,532"/>
      </g>
    </svg>
    <span class="abs dim-label" style="left:176px;top:133px">60 mm</span>
    <span class="abs dim-label" style="left:60px;top:346px">130 mm</span>

    <article class="abs label back-label" style="left:108px;top:169px;width:169px;height:367px;">
      <div class="abs variety-mark" style="left:11px;top:0;width:27px;height:34px;font-size:22px;padding:0 0 2px 4px;line-height:1;">F</div>
      <span class="abs variety-rest" style="left:40px;top:20px;font-size:10px;">ino</span>

      <div class="abs back-copy">
        <p>Lorem ipsum dolor sit amet, consectetur adipiscing elit. Mauris convallis, mauris nec maximus pretium, lectus nisl vestibulum nisi, sed posuere leo lacus id magna. Nulla ut orci ullamcorper, tristique metus quis, dictum nisl.</p>
        <p>Proin erat arcu, rhoncus a sem vitae, pulvinar porta nibh. Phasellus tortor augue, ornare rutrum tortor mattis, tincidunt finibus massa. Donec odio enim, tincidunt ac lectus ut, molestie ullamcorper elit. Donec cursus placerat auctor.</p>
        <p>Donec sit amet tortor ante. Donec a scelerisque nisl, id gravida lacus. Sed convallis magna libero, vitae vestibulum ligula laoreet vel. Proin quam mi, mattis interdum turpis eu, imperdiet vehicula velit.</p>
      </div>

      <svg class="abs" style="left:10px;top:266px" width="76" height="92" role="img" aria-label="Sellos de organismos colaboradores">
        <rect x="0" y="0" width="66" height="26" fill="#dfe8d9"/>
        <rect x="20" y="32" width="27" height="20" fill="#d7dbe6"/>
        <circle cx="13" cy="78" r="11" fill="#e2e2e2"/>
        <circle cx="53" cy="78" r="11" fill="#e2e2e2"/>
      </svg>

      <div class="abs" style="left:86px;top:267px;width:72px;height:93px;border:1px solid var(--amber);border-radius:5px;display:flex;align-items:center;justify-content:center;">
        <span class="seal-name">SELLORA</span>
      </div>
    </article>
  </section>

</main>
</body>
</html>
```